Home Services Website Design and Revisions

We have started to create a website but I would like to get some ideas and a quote on how to create a more professional website then what we have created thus far.

http://brinkhavenhomecare.example/

Pages I would need on the site

Home page - company summary and brand promise
who we are
what we do - services offered
our promise to quality and client experience
client experiences - testimonials and pictures
Promotions
Career opportunities - Join The team
Updates

Target Market(s)

Homeowners in the DFW region

Industry/Entity Type

Home Improvement

Number of Pages Required

5+ page

Font styles to use
Sans Serif

Requirements
Must have
• Home page - company summary and brand promise
• who we are
• what we do - services offered
• our promise to quality and client experience
• client experiences - testimonials and pictures
• Promotions
• Career opportunities - Join The team
• logo
• pictures
• links to social media sites
• A very impactful home page
• With a image of home and family.
• a beautiful home, yard and pictures of a loving family smiling and enjoying their home.
Nice to have
• Pictures with people to create emotion
• we don't work on houses
• we work on homes with families that trust us to provide quality services in a timely manner
• Families that trust us as their partner when they need work at their home with their family
Should not have
• low quality images or images just of homes

```html
<!DOCTYPE html>
<html lang="en">
<head>
<meta charset="utf-8">
<title>Brinkhaven Painting &amp; Home Services</title>
<link href="https://fonts.googleapis.com/css2?family=Oswald:wght@400;500&family=Rajdhani:wght@600;700&family=Open+Sans:ital,wght@0,400;0,600;0,700;1,400&display=swap" rel="stylesheet">
<style>
  :root {
    --orange: #f47a20;
    --green: #4caa3c;
    --ink: #1d1d1d;
    --text: #3a3a3a;
    --muted: #777;
    --light: #ececec;
    --footer: #e9e9e9;
    --bar: #2b2b2b;
    --white: #ffffff;
    --wall: #75667f;
    --wall-light: #9c8ea3;
    --floor: #8a6a4c;
    --skin: #e2b99a;
  }
  * { box-sizing: border-box; margin: 0; padding: 0; }
  html, body { width: 1200px; height: 2703px; overflow: hidden; }
  body { position: relative; background: var(--white); font-family: "Open Sans", Arial, sans-serif; color: var(--text); }

  /* Header */
  .site-header { position: absolute; left: 0; top: 0; width: 1200px; height: 209px; background: var(--white); }
  .brand { position: absolute; left: 105px; top: 82px; display: flex; align-items: center; gap: 12px; }
  .brand-square { width: 30px; height: 30px; background: var(--orange); }
  .brand-name { font-family: "Rajdhani", sans-serif; font-weight: 700; font-size: 52px; color: var(--ink); line-height: 1; }
  .call { position: absolute; left: 646px; top: 16px; font-size: 18px; color: var(--muted); }
  .call b { color: var(--ink); }
  .estimate { position: absolute; left: 930px; top: 10px; width: 150px; height: 40px; background: var(--green); color: var(--white); font-family: "Oswald", sans-serif; font-size: 18px; display: flex; align-items: center; justify-content: center; }
  .estimate::after { content: ""; position: absolute; right: -24px; top: 16px; width: 24px; height: 8px; background: var(--ink); }
  .social { position: absolute; left: 900px; top: 92px; display: flex; gap: 7px; }
  .social span { width: 40px; height: 40px; border-radius: 50%; display: block; }
  .s1 { background: #3b5998; } .s2 { background: #2fa6de; } .s3 { background: #d34836; } .s4 { background: #cb2027; } .s5 { background: var(--orange); }
  .main-nav { position: absolute; left: 345px; top: 158px; display: flex; gap: 33px; font-family: "Oswald", sans-serif; font-size: 20px; color: #444; text-transform: uppercase; }

  /* Hero photo area: room with purple walls, wood floor, family on the left */
  .hero { position: absolute; left: 0; top: 209px; width: 1200px; height: 634px; overflow: hidden;
    background:
      radial-gradient(ellipse 360px 300px at 330px 520px, rgba(226,185,154,.85) 0%, rgba(160,190,215,.55) 45%, rgba(160,190,215,0) 75%),
      radial-gradient(ellipse 180px 250px at 1020px 420px, rgba(90,130,60,.75) 0%, rgba(90,130,60,0) 70%),
      radial-gradient(ellipse 380px 150px at 840px 490px, rgba(80,78,76,.8) 0%, rgba(80,78,76,0) 75%),
      linear-gradient(90deg, rgba(235,232,228,.9) 0px, rgba(235,232,228,.35) 170px, rgba(235,232,228,0) 260px),
      linear-gradient(180deg, #d8d3d6 0px, #d8d3d6 26px, var(--wall-light) 40px, var(--wall) 180px, var(--wall) 450px, #a08062 500px, var(--floor) 634px);
  }
  .hero-arrow { position: absolute; top: 268px; width: 40px; height: 98px; background: #222; display: flex; align-items: center; justify-content: center; }
  .hero-arrow.left { left: 0; } .hero-arrow.right { right: 0; }

  /* Intro columns */
  .intro { position: absolute; left: 0; top: 843px; width: 1200px; height: 395px; }
  .intro-col { position: absolute; top: 52px; width: 300px; text-align: center; }
  .col-title { font-family: "Rajdhani", sans-serif; font-weight: 700; font-size: 26px; color: var(--ink); display: flex; align-items: center; justify-content: center; gap: 8px; }
  .col-title::before { content: ""; width: 16px; height: 16px; background: var(--orange); }
  .intro-col p { margin-top: 14px; font-size: 14px; line-height: 24px; color: var(--text); }
  .btn-more { display: inline-block; margin-top: 16px; padding: 0 22px; height: 30px; line-height: 30px; border-radius: 15px; background: var(--orange); color: var(--white); font-size: 12px; font-weight: 600; text-transform: uppercase; }

  /* Featured services */
  .featured { position: absolute; left: 0; top: 1238px; width: 1200px; height: 674px; background: var(--light); }
  .featured-title { position: absolute; left: 0; top: 85px; width: 1200px; text-align: center; font-family: "Rajdhani", sans-serif; font-weight: 700; font-size: 34px; color: var(--ink); }
  .service-card { position: absolute; top: 183px; width: 240px; height: 300px; background: var(--white); border-bottom: 3px solid #333; box-shadow: 0 2px 6px rgba(0,0,0,.12); }
  .service-card .photo { position: absolute; left: 12px; top: 12px; width: 216px; height: 210px; }
  .service-card h3 { position: absolute; left: 12px; top: 236px; font-family: "Rajdhani", sans-serif; font-weight: 700; font-size: 19px; line-height: 21px; color: var(--ink); text-transform: uppercase; }
  .service-card .hook { position: absolute; left: 111px; top: 300px; width: 18px; height: 36px; background: #222; }
  .service-card .tag { position: absolute; left: 104px; top: -40px; width: 32px; height: 32px; background: var(--orange); }
  .photo-exterior { background: radial-gradient(ellipse 130px 70px at 110px 125px, #b99f82 0%, rgba(185,159,130,0) 100%), linear-gradient(180deg, #9fbfdc 0%, #c9d9e6 35%, #b49d83 55%, #8c7d6c 85%, #a7a39e 100%); }
  .photo-interior { background: radial-gradient(ellipse 70px 50px at 150px 120px, #f2eee6 0%, rgba(242,238,230,0) 100%), linear-gradient(180deg, #d3c9b7 0%, #c2b59e 58%, #8a5533 70%, #6a3c22 100%); }
  .photo-lawn { background: radial-gradient(ellipse 90px 70px at 100px 80px, #d32f2a 0%, #d32f2a 40%, rgba(211,47,42,0) 100%), radial-gradient(ellipse 40px 40px at 160px 150px, #e4e4e4 0%, rgba(228,228,228,0) 100%), linear-gradient(160deg, #6aa13f 0%, #4f8a2e 100%); }
  .photo-window { background: radial-gradient(ellipse 90px 110px at 150px 90px, #b7c6d2 0%, rgba(183,198,210,0) 100%), linear-gradient(180deg, #a6c1da 0%, #9c8b76 30%, #7b6a58 75%, #5a4c40 100%); }
  .car-arrow { position: absolute; top: 318px; }
  .featured-copy { position: absolute; left: 110px; top: 548px; width: 980px; text-align: center; font-size: 20px; line-height: 25px; color: #8a8a8a; }

  /* Guarantee band */
  .guarantee { position: absolute; left: 0; top: 1912px; width: 1200px; height: 156px; display: flex; align-items: center; justify-content: center; gap: 30px; }
  .guarantee h2 { font-family: "Rajdhani", sans-serif; font-weight: 700; font-size: 50px; color: var(--bar); letter-spacing: 1px; }
  .phone-pill { height: 46px; padding: 0 22px 0 18px; border-radius: 23px; background: var(--orange); color: var(--white); font-family: "Rajdhani", sans-serif; font-weight: 700; font-size: 30px; display: flex; align-items: center; gap: 8px; }

  /* Testimonial */
  .testimonial { position: absolute; left: 0; top: 2068px; width: 1200px; height: 292px; background: linear-gradient(180deg, #7b7b7b 0%, #a6a6a6 100%); }
  .testimonial .photo { position: absolute; left: 50px; top: -14px; width: 370px; height: 306px;
    background:
      radial-gradient(ellipse 120px 90px at 150px 80px, rgba(226,185,154,.95) 0%, rgba(226,185,154,0) 100%),
      radial-gradient(ellipse 110px 90px at 240px 120px, rgba(230,195,160,.9) 0%, rgba(230,195,160,0) 100%),
      radial-gradient(ellipse 190px 140px at 170px 250px, rgba(175,200,225,.95) 0%, rgba(175,200,225,0) 100%),
      radial-gradient(ellipse 130px 110px at 270px 260px, rgba(240,240,240,.9) 0%, rgba(240,240,240,0) 100%); }
  .testimonial h2 { position: absolute; left: 432px; top: 48px; font-family: "Rajdhani", sans-serif; font-weight: 700; font-size: 24px; color: var(--white); }
  .testimonial blockquote { position: absolute; left: 432px; top: 92px; width: 700px; font-style: italic; font-size: 18px; line-height: 28px; color: var(--white); }
  .testimonial .author { position: absolute; left: 432px; top: 224px; font-size: 13px; font-weight: 600; color: var(--white); }
  .testimonial .read-full { position: absolute; left: 951px; top: 224px; font-size: 13px; color: var(--white); text-transform: uppercase; }

  /* Footer */
  .site-footer { position: absolute; left: 0; top: 2360px; width: 1200px; height: 300px; background: var(--footer); }
  .foot-col { position: absolute; top: 52px; font-size: 13px; color: var(--text); }
  .foot-col h4 { font-size: 13px; font-weight: 700; color: var(--ink); text-transform: uppercase; margin-bottom: 16px; }
  .foot-links li { list-style: none; line-height: 26px; }
  .foot-links li::before { content: "›"; margin-right: 8px; }
  .contact p { line-height: 20px; margin-bottom: 18px; }
  .inquiry input, .inquiry .msg { display: block; width: 242px; height: 32px; margin-bottom: 7px; background: var(--white); border: 1px solid #d5d5d5; padding: 0 8px; font: 13px "Open Sans", sans-serif; color: var(--muted); line-height: 30px; }
  .inquiry .msg { height: 62px; }
  .inquiry .submit { width: 242px; height: 32px; background: var(--orange); color: var(--white); font-size: 13px; font-weight: 600; text-align: center; line-height: 32px; }
  .follow li { list-style: none; display: flex; align-items: center; gap: 12px; height: 36px; }
  .follow li span { width: 28px; height: 28px; border-radius: 50%; display: block; }
  .foot-brand { position: absolute; left: 912px; top: 110px; display: flex; align-items: center; gap: 10px; }
  .foot-brand .brand-name { font-size: 40px; }
  .foot-brand .brand-square { width: 24px; height: 24px; }
  .bottom-bar { position: absolute; left: 0; top: 2660px; width: 1200px; height: 43px; background: var(--bar); color: var(--white); font-size: 13px; display: flex; align-items: center; justify-content: center; }
</style>
</head>
<body>

<header class="site-header">
  <div class="brand"><span class="brand-square"></span><span class="brand-name">Brinkhaven</span></div>
  <div class="call">Call Today!: <b>555.010.2284</b></div>
  <div class="estimate">FREE ESTIMATE</div>
  <div class="social"><span class="s1"></span><span class="s2"></span><span class="s3"></span><span class="s4"></span><span class="s5"></span></div>
  <nav class="main-nav">
    <span>Home</span><span>Who We Are</span><span>What We Do</span><span>Testimonials</span><span>Promotions</span><span>Career</span><span>Contact Us</span>
  </nav>
</header>

<section class="hero" role="img" aria-label="Photo: smiling family of four together in their bright living room with purple walls, a grey sofa, a potted tree and a wood floor">
  <div class="hero-arrow left"><svg width="16" height="22"><path d="M13 2 L3 11 L13 20" stroke="#fff" stroke-width="4" fill="none"/></svg></div>
  <div class="hero-arrow right"><svg width="16" height="22"><path d="M3 2 L13 11 L3 20" stroke="#fff" stroke-width="4" fill="none"/></svg></div>
</section>

<section class="intro">
  <div class="intro-col" style="left:90px">
    <h2 class="col-title">ABOUT US</h2>
    <p>Welcome to Brinkhaven Home Services and Painting Specialists. We are committed to providing reliable TRUSTED home services for you and your family. We are home service experts with decades of home service leadership and expertise. Our management team has delivered quality services to...</p>
    <span class="btn-more">Read More</span>
  </div>
  <div class="intro-col" style="left:450px">
    <h2 class="col-title">WHO WE ARE</h2>
    <p>Lorem ipsum dolor sit amet, consectetur adipiscing elit, sed do eiusmod tempor incididunt ut labore et dolore magna aliqua. Ut enim ad minim veniam, quis nostrud exercitation ullamco laboris nisi ut aliquip ex ea commodo consequat. quis nostrud exercitation ullamco laboris nisi ut aliquip...</p>
    <span class="btn-more">Read More</span>
  </div>
  <div class="intro-col" style="left:810px">
    <h2 class="col-title">WHAT WE DO</h2>
    <p>Lorem ipsum dolor sit amet, consectetur adipiscing elit, sed do eiusmod tempor incididunt ut labore et dolore magna aliqua. Ut enim ad minim veniam, quis nostrud exercitation ullamco laboris nisi ut aliquip ex ea commodo consequat. quis nostrud exercitation ullamco laboris nisi ut aliquip...</p>
    <span class="btn-more">Read More</span>
  </div>
</section>

<section class="featured">
  <h2 class="featured-title">FEATURED SERVICES</h2>
  <svg class="car-arrow" style="left:72px" width="20" height="30"><path d="M16 3 L5 15 L16 27" stroke="#333" stroke-width="4" fill="none"/></svg>
  <svg class="car-arrow" style="left:1106px" width="20" height="30"><path d="M4 3 L15 15 L4 27" stroke="#333" stroke-width="4" fill="none"/></svg>

  <article class="service-card" style="left:103px">
    <span class="tag"></span>
    <div class="photo photo-exterior" role="img" aria-label="Photo: large stone family home exterior under a blue sky"></div>
    <h3>Exterior Residential<br>Painting</h3><span class="hook"></span>
  </article>
  <article class="service-card" style="left:353px">
    <span class="tag"></span>
    <div class="photo photo-interior" role="img" aria-label="Photo: freshly painted living room with fireplace and hardwood floor"></div>
    <h3>Interior Residential<br>Painting</h3><span class="hook"></span>
  </article>
  <article class="service-card" style="left:603px">
    <span class="tag"></span>
    <div class="photo photo-lawn" role="img" aria-label="Photo: red lawn mower on freshly cut green grass"></div>
    <h3>Landscaping<br>Services</h3><span class="hook"></span>
  </article>
  <article class="service-card" style="left:853px">
    <span class="tag"></span>
    <div class="photo photo-window" role="img" aria-label="Photo: worker on a ladder washing the windows of a stone home"></div>
    <h3>Window<br>Washing</h3><span class="hook"></span>
  </article>

  <p class="featured-copy">Our leadership team has managed over $75,000,000 worth of residential home services. Our mission is to become your trusted call when you need work done at your home. To be the partner you trust to deliver quality services using only top of the line products</p>
</section>

<section class="guarantee">
  <h2>GUARANTEED AWESOME</h2>
  <div class="phone-pill">
    <svg width="22" height="22" viewBox="0 0 24 24"><path d="M6.6 10.8a15 15 0 0 0 6.6 6.6l2.2-2.2a1 1 0 0 1 1-.25 11.4 11.4 0 0 0 3.6.57 1 1 0 0 1 1 1V20a1 1 0 0 1-1 1A17 17 0 0 1 3 4a1 1 0 0 1 1-1h3.5a1 1 0 0 1 1 1c0 1.25.2 2.45.57 3.6a1 1 0 0 1-.25 1z" fill="#fff"/></svg>
    555.010.2284
  </div>
</section>

<section class="testimonial">
  <div class="photo" role="img" aria-label="Photo: happy couple giving a thumbs up"></div>
  <h2>WHAT OUR CUSTOMERS HAVE TO SAY</h2>
  <blockquote>“Lorem ipsum dolor sit amet, consectetur adipiscing elit, sed do eiusmod tempor incididunt ut labore et dolore magna aliqua. Ut enim ad minim veniam, quis nostrud exercitation ullamco laboris nisi ut aliquip ex ea commodo consequat.” Duis aute irure dolor in reprehenderit in voluptate velit esse cillum dolore eu fugiat.</blockquote>
  <div class="author">- Dana</div>
  <div class="read-full">Read Full Testimonial ›</div>
</section>

<footer class="site-footer">
  <div class="foot-col" style="left:73px">
    <h4>Quick Links</h4>
    <ul class="foot-links">
      <li>Home</li><li>Who We Are</li><li>What We Do</li><li>Testimonials</li><li>Promotions</li><li>Career</li><li>Contact Us</li>
    </ul>
  </div>
  <div class="foot-col contact" style="left:216px;width:240px">
    <h4>Contact Detail</h4>
    <p>Contact your home service provider now!</p>
    <p>Office:<br>555.010.2284</p>
    <p>Email:<br>hello@brinkhavenhomecare.example</p>
  </div>
  <div class="foot-col inquiry" style="left:478px">
    <h4>Quick Inquiry</h4>
    <div class="inquiry"><input value="Name" readonly><input value="Phone" readonly><div class="msg">Message</div><div class="submit">SUBMIT</div></div>
  </div>
  <div class="foot-col" style="left:761px">
    <h4>Follow Us</h4>
    <ul class="follow">
      <li><span class="s1"></span>Friendbook</li>
      <li><span class="s2"></span>Chirper</li>
      <li><span class="s3"></span>Circles +</li>
      <li><span class="s4"></span>Pinboard</li>
      <li><span class="s5"></span>Share</li>
    </ul>
  </div>
  <div class="foot-brand"><span class="brand-square"></span><span class="brand-name">Brinkhaven</span></div>
</footer>

<div class="bottom-bar">© 2016 Brinkhaven Painting &amp; Home Services. All Rights Reserved &nbsp;|&nbsp; Privacy Policy</div>

</body>
</html>
```